BrambleWorks business card

Looking for business card design that supports our company/software values. We have 2 logo designs at the moment but open to change if you think you can enhance the brand. Check out website www.brambleworks.com.au.

Target Market(s)

Education

Contact Information for Business Card

Name, title, mobile, email and website

Font styles to use
Sans Serif

Colors

Designer to choose colors to be used in the design.

Requirements
Must have
• BrambleWorks logo with tree and tagline on rear side with dark grey background colour

```html
<!DOCTYPE html>
<html lang="en">
<head>
<meta charset="utf-8">
<title>BrambleWorks Business Card</title>
<link href="https://fonts.googleapis.com/css2?family=Roboto:wght@300;400;500&display=swap" rel="stylesheet">
<style>
  :root {
    --backdrop: #bdbdbd;
    --paper: #ffffff;
    --charcoal: #4d4d4c;
    --ink: #4a4a4a;
    --leaf: #336b0e;
  }
  * { box-sizing: border-box; margin: 0; padding: 0; }
  html, body {
    width: 1200px;
    height: 1200px;
    overflow: hidden;
    background: var(--backdrop);
    font-family: "Roboto", Arial, sans-serif;
  }
  .canvas {
    width: 1200px;
    height: 1200px;
    display: flex;
    flex-direction: column;
    align-items: center;
    justify-content: center;
    gap: 60px;
  }
  .card {
    position: relative;
    width: 910px;
    height: 520px;
    overflow: hidden;
    box-shadow: 0 10px 30px rgba(0,0,0,0.18);
  }

  /* Front */
  .card--front { background: var(--paper); }
  .card--front .brand-area {
    position: absolute;
    left: 0; top: 0;
    width: 100%;
    height: 300px;
    display: flex;
    align-items: center;
    justify-content: center;
    gap: 34px;
  }
  .brand-mark {
    width: 120px;
    height: 120px;
    border-radius: 50%;
    background: var(--charcoal);
    flex: none;
  }
  .brand-lockup { display: flex; flex-direction: column; }
  .brand-name {
    font-size: 76px;
    font-weight: 400;
    line-height: 1;
    letter-spacing: 1px;
    color: var(--ink);
    padding-bottom: 10px;
    border-bottom: 2px solid var(--ink);
  }
  .brand-tagline {
    margin-top: 8px;
    font-size: 30px;
    font-weight: 300;
    letter-spacing: 1px;
    color: var(--ink);
  }
  .card--front .values-band {
    position: absolute;
    left: 0; top: 300px;
    width: 100%;
    height: 62px;
    background: var(--charcoal);
    color: var(--paper);
  }
  .values-band, .values-strip {
    display: flex;
    align-items: center;
    justify-content: center;
    font-size: 28px;
    font-weight: 500;
    letter-spacing: 0.5px;
    text-transform: uppercase;
  }
  .card--front .web {
    position: absolute;
    left: 0; top: 382px;
    width: 100%;
    text-align: center;
    font-size: 30px;
    font-weight: 400;
    color: var(--leaf);
  }

  /* Back */
  .card--back { background: var(--charcoal); }
  .card--back .brand-area {
    position: absolute;
    left: 0; top: 0;
    width: 100%;
    height: 280px;
    display: flex;
    align-items: center;
    justify-content: center;
    gap: 34px;
  }
  .card--back .brand-mark { background: var(--paper); }
  .card--back .brand-name { color: var(--paper); border-bottom-color: var(--paper); }
  .card--back .brand-tagline { color: var(--paper); }
  .card--back .values-strip {
    position: absolute;
    left: 0; top: 280px;
    width: 100%;
    height: 64px;
    background: var(--paper);
    color: var(--ink);
  }
  .card--back .web {
    position: absolute;
    left: 0; top: 392px;
    width: 100%;
    text-align: center;
    font-size: 30px;
    font-weight: 400;
    color: var(--paper);
  }
</style>
</head>
<body>
<main class="canvas">
  <section class="card card--front" aria-label="Business card front">
    <div class="brand-area">
      <span class="brand-mark" aria-hidden="true"></span>
      <div class="brand-lockup">
        <span class="brand-name">BrambleWorks</span>
        <span class="brand-tagline">Student Success Platform</span>
      </div>
    </div>
    <div class="values-band">Discovery • Insights • Case Management • Engage</div>
    <p class="web">www.brambleworks.com.au.</p>
  </section>

  <section class="card card--back" aria-label="Business card back">
    <div class="brand-area">
      <span class="brand-mark" aria-hidden="true"></span>
      <div class="brand-lockup">
        <span class="brand-name">BrambleWorks</span>
        <span class="brand-tagline">Student Success Platform</span>
      </div>
    </div>
    <div class="values-strip">Discovery • Insights • Case Management • Engage</div>
    <p class="web">www.brambleworks.com.au.</p>
  </section>
</main>
</body>
</html>
```